Policies Manual Design & Formatting

My company currently has complete bylaws and policies organized as needed. We would like them formatted in Word to look professional and easily editable.

We have all text and titles completed and a brand book to guide text and colors. We would also like the designer to gather design inspiration from our website brackenfordguild.org.

Text word file upload coming on 10/18
Updates

Went on vacation/holiday

Industry/Entity Type

Business Consultant

Font styles to use
Serif
Sans Serif
Other font styles liked:
• Montserrat and Domine

Colors

Designer to choose colors to be used in the design.

Requirements
Must have
• Montserrat and domine fonts
• Colors from brand book file
• layout and print formatting
• dynamic Table of Contents
• Incorporate logo and company information
• Include automatic page numbers
• Modify or add headers/footer
• Profeasional cover page

```html
<!DOCTYPE html>
<html lang="en">
<head>
<meta charset="utf-8">
<title>Policies Manual – Page 2</title>
<link rel="stylesheet" href="https://fonts.googleapis.com/css2?family=Montserrat:wght@400;700&display=swap">
<style>
  :root {
    --paper: #ffffff;
    --ink: #3c3c3c;
    --heading-ink: #2e2e2e;
    --brand-blue: #1f8fc8;
    --footer-charcoal: #3a3e41;
  }
  * { margin: 0; padding: 0; box-sizing: border-box; }
  html, body {
    width: 853px;
    height: 1200px;
    overflow: hidden;
    background: var(--paper);
  }
  .page {
    position: relative;
    width: 853px;
    height: 1200px;
    background: var(--paper);
    overflow: hidden;
    font-family: "Montserrat", Arial, sans-serif;
  }
  .footer-band {
    position: absolute;
    left: 0;
    right: 0;
    top: 1044px;
    height: 76px;
    background: var(--footer-charcoal);
  }
  .side-band {
    position: absolute;
    top: 0;
    bottom: 0;
    left: 665px;
    width: 80px;
    background: var(--brand-blue);
  }
  .page-number {
    position: absolute;
    left: 665px;
    width: 80px;
    top: 1074px;
    text-align: center;
    font-weight: 700;
    font-size: 30px;
    color: var(--footer-charcoal);
  }
  .section {
    position: absolute;
    left: 71px;
    top: 62px;
    width: 548px;
    color: var(--ink);
  }
  .section-title {
    font-weight: 700;
    font-size: 17px;
    color: var(--heading-ink);
    margin-bottom: 22px;
  }
  .section-body {
    font-weight: 400;
    font-size: 15.2px;
    line-height: 20.5px;
  }
</style>
</head>
<body>
  <main class="page">
    <div class="footer-band"></div>
    <div class="side-band"></div>
    <div class="page-number">2</div>

    <section class="section">
      <h2 class="section-title">1.4: Limitation of Methods</h2>
      <p class="section-body">The Chamber shall observe all local, state and federal laws, rules, and regulations that apply to a non-profit business incorporated under Oregon Revised Statute Chapter 65 and exempt from income tax under Section501(c)(6) of the Internal Revenue Code. The Chamber shall comply with Internal Revenue Code section 501(c)(6) and rules and regulations thereunder prior to lending its influence or facilities, either directly or indirectly, to the nomination, election, or appointment of any candidate for public office or engaging in legislative activities on a federal or state-wide basis.</p>
    </section>
  </main>
</body>
</html>
```